New Look and Feel for 82 year old Varrenko Ltd. presentations

We are seeking new ideas to have powerpoint-layouts for the group headquarters. Varrenko is an industrial company in maritime, hydraulics, heavy machinery and industrial services. Please read our history and watch the video for a quick familiarization. http://www.varrenko-example.fi/eng/main.php

Our customer relationships are based on trust, with Varrenko providing to customers, cooperation partners and other interest groups products and solutions that produce sustainable benefits.

Varrenko strives to ensure that the environmental impact of the products is considered over the entire life cycle and the processes used by the Group are as environmentally benign as possible.

Industry/Entity Type

It Company

Colors

Designer to choose colors to be used in the design.

Requirements
Must have
• Logo
Nice to have
• example animations and transitions

```html
<!DOCTYPE html>
<html lang="en">
<head>
<meta charset="utf-8">
<title>Varrenko Ltd. — Presentation Layouts</title>
<link rel="stylesheet" href="https://fonts.googleapis.com/css2?family=Raleway:wght@400;600;700;800&family=Open+Sans:wght@400;600;700&display=swap">
<style>
:root{
  --red:#e2474b;
  --ink:#3b3b3d;
  --ink-deep:#2a2a2c;
  --grey:#8c8c8e;
  --grey-mid:#b5b5b7;
  --grey-light:#e9e9ea;
  --grey-pale:#f4f4f5;
  --paper:#ffffff;
}
*{box-sizing:border-box;margin:0;padding:0}
html,body{width:1200px;height:4810px;overflow:hidden;background:#fff}
body{font-family:"Open Sans",Arial,sans-serif;color:var(--ink)}
.deck{display:grid;grid-template-columns:repeat(3,392px);grid-auto-rows:287.5px;gap:14px 12px;width:1200px;height:4810px}
.slide{position:relative;overflow:hidden;background:var(--paper);box-shadow:0 0 0 1px #ececec}
.slide.dark{background:var(--ink)}
.slide.red{background:var(--red)}
.slide.grey{background:#77777a}
.title{position:absolute;left:16px;top:14px;font-family:"Raleway",sans-serif;font-weight:700;font-size:14px;color:var(--ink)}
.dark .title{color:#fff}
.logo{position:absolute;right:14px;top:13px;display:flex;align-items:center;gap:3px;font-family:"Raleway",sans-serif;font-weight:800;font-size:7px;color:var(--red)}
.logo-mark{width:10px;height:10px;background:var(--red)}
.brand-block{position:absolute;background:var(--red);display:flex;flex-direction:column;align-items:center;justify-content:center;gap:5px;font-family:"Raleway",sans-serif;font-weight:800;color:#fff}
.brand-block .mark{background:#fff}
.footer{position:absolute;left:0;right:0;bottom:4px;height:8px}
.footer::before,.footer::after{content:"";position:absolute;left:0;right:0;height:2px}
.footer::before{top:1px;background:var(--ink)}
.footer::after{top:5px;background:var(--red)}
.footer .mini{position:absolute;left:50%;top:-2px;width:12px;height:12px;margin-left:-6px;background:var(--red);box-shadow:0 0 0 2px #fff}
.dark .footer::before,.red .footer::before,.grey .footer::before{background:#9a9a9c}
.dark .footer .mini,.red .footer .mini,.grey .footer .mini{box-shadow:0 0 0 2px var(--ink)}
.photo{position:absolute;background:linear-gradient(135deg,#5a5c60,#2f3034 70%,#7a4441)}
.photo.light{background:linear-gradient(135deg,#e1e3e6,#a9adb2)}
.photo.warm{background:linear-gradient(135deg,#9a7a62,#3c3633)}
.photo.round{border-radius:50%}
.map{position:absolute;background:linear-gradient(160deg,#e4e4e6,#cfcfd2)}
.txt{position:absolute;font-size:6px;line-height:1.55;color:var(--grey)}
.dark .txt{color:#c9c9cb}
.h{font-family:"Raleway",sans-serif;font-weight:700;color:var(--ink);font-size:7px}
.dot{position:absolute;border-radius:50%;background:var(--red);display:flex;align-items:center;justify-content:center;color:#fff;font-family:"Raleway",sans-serif;font-weight:700;font-size:7px}
.dot.ink{background:var(--ink)}
.dot.grey{background:var(--grey-mid)}
.big{font-family:"Raleway",sans-serif;font-weight:700}
.lbl{position:absolute;font-size:6px;color:var(--grey);line-height:1.5}
.sec-title{position:absolute;font-family:"Raleway",sans-serif;font-weight:700;font-size:13px;color:#fff}
.shape{position:absolute;background:var(--ink)}
svg{position:absolute;overflow:visible}
table{border-collapse:collapse}
td,th{padding:0 6px;text-align:left}
</style>
</head>
<body>
<main class="deck">

<!-- 1 cover -->
<section class="slide">
  <div class="photo light" style="left:0;top:0;width:392px;height:105px" role="img" aria-label="Pale industrial workshop photo"></div>
  <div style="position:absolute;left:0;top:105px;width:392px;height:34px;background:var(--ink)"></div>
  <div class="brand-block" style="left:18px;top:90px;width:62px;height:60px;font-size:8px"><span class="mark" style="width:16px;height:16px"></span>Varrenko</div>
  <div class="big" style="position:absolute;left:28px;top:166px;font-size:17px;color:var(--red)">Your Title Goes Here</div>
  <div class="txt" style="left:28px;top:190px;color:var(--red)">Your Subtitle Goes Here</div>
  <div class="footer"><span class="mini"></span></div>
</section>

<!-- 2 cover dark -->
<section class="slide dark">
  <div class="photo" style="inset:0" role="img" aria-label="Dark close-up of heavy machinery"></div>
  <div class="brand-block" style="left:0;top:96px;width:92px;height:80px;font-size:9px"><span class="mark" style="width:22px;height:22px"></span>Varrenko</div>
  <div class="big" style="position:absolute;left:108px;top:118px;font-size:17px;color:#fff">Your Title Goes Here</div>
  <div class="txt" style="left:108px;top:142px;color:#fff">Your Subtitle Goes Here</div>
</section>

<!-- 3 agenda -->
<section class="slide">
  <div class="title">Our Agenda</div>
  <div class="dot ink" style="left:36px;top:56px;width:16px;height:16px">1</div><div class="txt" style="left:60px;top:55px"><span class="h">Company History</span><br>Our roots and values</div>
  <div class="dot" style="left:210px;top:56px;width:16px;height:16px">2</div><div class="txt" style="left:234px;top:55px"><span class="h">Markets Served</span><br>Key figures of the year</div>
  <div class="dot ink" style="left:36px;top:116px;width:16px;height:16px">3</div><div class="txt" style="left:60px;top:115px"><span class="h">Maritime Unit</span><br>New vessel projects</div>
  <div class="dot" style="left:210px;top:116px;width:16px;height:16px">4</div><div class="txt" style="left:234px;top:115px"><span class="h">Hydraulics Unit</span><br>Partners and growth</div>
  <div class="dot ink" style="left:36px;top:176px;width:16px;height:16px">5</div><div class="txt" style="left:60px;top:175px"><span class="h">Services</span><br>Full life cycle support</div>
  <div class="dot" style="left:210px;top:176px;width:16px;height:16px">6</div><div class="txt" style="left:234px;top:175px"><span class="h">Outlook</span><br>Plans and questions</div>
  <div class="footer"><span class="mini"></span></div>
</section>

<!-- 4 title image text -->
<section class="slide">
  <div class="title">Title And Image + Text</div>
  <div class="logo"><span class="logo-mark"></span>Varrenko</div>
  <div class="photo" style="left:16px;top:44px;width:360px;height:92px" role="img" aria-label="Factory hall with machinery"></div>
  <div class="brand-block" style="left:170px;top:56px;width:90px;height:66px;font-size:10px"><span class="mark" style="width:20px;height:20px"></span>Varrenko</div>
  <div class="txt" style="left:16px;top:150px;width:130px">Varrenko builds reliable machines for maritime and heavy industry across Europe, with service that lasts.</div>
  <div class="footer"><span class="mini"></span></div>
</section>

<!-- 5 icon slide -->
<section class="slide">
  <div class="title">Icon Slide</div>
  <div class="photo" style="left:235px;top:0;width:157px;height:270px" role="img" aria-label="Engineer at work in a plant"></div>
  <div class="txt" style="left:110px;top:62px;width:100px;text-align:right"><span class="h">Quality</span><br>Tested in every step</div><div class="dot" style="left:222px;top:64px;width:26px;height:26px">✓</div>
  <div class="txt" style="left:110px;top:117px;width:100px;text-align:right"><span class="h">Service</span><br>Support on all sites</div><div class="dot" style="left:222px;top:119px;width:26px;height:26px">✓</div>
  <div class="txt" style="left:110px;top:172px;width:100px;text-align:right"><span class="h">Safety</span><br>People come first</div><div class="dot" style="left:222px;top:174px;width:26px;height:26px">✓</div>
  <div class="footer"><span class="mini"></span></div>
</section>

<!-- 6 your title here -->
<section class="slide">
  <div class="title">Your Title Here</div>
  <div class="logo"><span class="logo-mark"></span>Varrenko</div>
  <div class="photo warm" style="left:0;top:44px;width:392px;height:108px" role="img" aria-label="Yellow machinery on a production line"></div>
  <div class="txt" style="left:16px;top:165px;width:200px">Sustainable benefits for customers and partners through durable products and trusted cooperation.</div>
  <div class="footer"><span class="mini"></span></div>
</section>

<!-- 7 about us -->
<section class="slide">
  <div class="photo light" style="left:0;top:0;width:170px;height:270px" role="img" aria-label="Worker in hard hat and safety gear"></div>
  <div style="position:absolute;left:170px;top:70px;width:222px;height:120px;background:var(--ink)"></div>
  <div class="big" style="position:absolute;left:190px;top:88px;font-size:14px;color:#fff">About Us</div>
  <div class="txt" style="left:190px;top:112px;width:180px;color:#ccc">Founded 82 years ago, we serve maritime, hydraulics and heavy machinery customers with care.</div>
  <div class="logo"><span class="logo-mark"></span>Varrenko</div>
  <div class="footer"><span class="mini"></span></div>
</section>

<!-- 8 about us dark -->
<section class="slide dark">
  <div class="title">About Us</div>
  <div class="photo light round" style="left:166px;top:56px;width:62px;height:62px;border:3px solid #fff" role="img" aria-label="Portrait photo of a team member"></div>
  <div class="txt" style="left:86px;top:130px;width:220px;text-align:center">Trust based relationships with customers, partners and all interest groups we work with.</div>
  <div class="dot grey" style="left:174px;top:162px;width:9px;height:9px"></div>
  <div class="dot grey" style="left:192px;top:162px;width:9px;height:9px"></div>
  <div class="dot grey" style="left:210px;top:162px;width:9px;height:9px"></div>
  <div class="footer"><span class="mini"></span></div>
</section>

<!-- 9 title + monitor -->
<section class="slide">
  <div class="big" style="position:absolute;left:16px;top:40px;font-size:14px;color:var(--ink);width:120px;line-height:1.2">Your Title Goes Here</div>
  <div class="txt" style="left:16px;top:84px;width:120px">Environmentally benign processes across the whole product life cycle.</div>
  <div style="position:absolute;left:150px;top:58px;width:226px;height:130px;background:var(--ink-deep);border-radius:4px;padding:6px"><div class="photo warm" style="position:relative;width:100%;height:100%" role="img" aria-label="Welder at work shown on a monitor screen"></div></div>
  <div style="position:absolute;left:250px;top:188px;width:26px;height:12px;background:var(--grey-mid)"></div>
  <div style="position:absolute;left:236px;top:200px;width:54px;height:3px;background:var(--grey-mid)"></div>
  <div class="logo"><span class="logo-mark"></span>Varrenko</div>
  <div class="footer"><span class="mini"></span></div>
</section>

<!-- 10 section break -->
<section class="slide dark">
  <div class="brand-block" style="left:20px;top:130px;width:82px;height:62px;font-size:9px"><span class="mark" style="width:18px;height:18px"></span>Varrenko</div>
  <div style="position:absolute;left:0;top:192px;width:392px;height:10px;background:var(--red)"></div>
  <div class="sec-title" style="left:20px;top:212px">Section Break</div>
  <div class="footer"><span class="mini"></span></div>
</section>

<!-- 11 title image text -->
<section class="slide">
  <div class="title">Title And Image + Text</div>
  <div class="logo"><span class="logo-mark"></span>Varrenko</div>
  <div class="photo" style="left:16px;top:44px;width:160px;height:130px" role="img" aria-label="Rotating machine part close-up"></div>
  <div style="position:absolute;left:176px;top:60px;width:200px;height:100px;background:var(--ink)"></div>
  <div class="txt" style="left:190px;top:74px;width:170px;color:#ddd">Long term cooperation produces lasting value for every interest group we serve.</div>
  <div class="txt" style="left:16px;top:190px;width:360px">Our processes are designed to be as environmentally benign as possible, from design to recycling.</div>
  <div class="footer"><span class="mini"></span></div>
</section>

<!-- 12 about us grey -->
<section class="slide">
  <div class="title">About Us</div>
  <div class="logo"><span class="logo-mark"></span>Varrenko</div>
  <div class="photo warm" style="left:16px;top:50px;width:170px;height:130px" role="img" aria-label="Hands working on a metal part"></div>
  <div style="position:absolute;left:210px;top:40px;width:182px;height:220px;background:var(--grey)"></div>
  <div class="txt" style="left:224px;top:60px;width:150px;color:#f2f2f2">We deliver industrial services with care for people and the environment in every project.</div>
  <div class="footer"><span class="mini"></span></div>
</section>

<!-- 13 company details -->
<section class="slide">
  <div class="title">Company Details</div>
  <div class="txt" style="left:16px;top:50px;width:160px"><span class="h">Varrenko Ltd.</span><br>Maritime solutions<br>Hydraulics<br>Heavy machinery<br>Industrial services<br>varrenko-example.fi</div>
  <div class="brand-block" style="left:210px;top:70px;width:150px;height:110px;font-size:14px"><span class="mark" style="width:30px;height:30px"></span>Varrenko</div>
  <div class="footer"><span class="mini"></span></div>
</section>

<!-- 14 blank -->
<section class="slide">
  <div class="title">Your Blank Slide</div>
  <div class="footer"><span class="mini"></span></div>
</section>

<!-- 15 portfolio -->
<section class="slide">
  <div class="shape" style="left:18px;top:24px;width:62px;height:18px"></div>
  <div class="shape" style="left:140px;top:22px;width:70px;height:22px;border-radius:11px"></div>
  <div class="shape" style="left:236px;top:20px;width:40px;height:26px;background:transparent;border:2px solid var(--ink)"></div>
  <div class="shape" style="left:318px;top:12px;width:42px;height:42px;border-radius:50%"></div>
  <div class="shape" style="left:18px;top:92px;width:66px;height:28px;background:transparent;border:2px solid var(--ink)"></div>
  <div class="shape" style="left:110px;top:82px;width:170px;height:78px"></div>
  <div class="big" style="position:absolute;left:110px;width:170px;top:110px;text-align:center;font-size:15px;color:#fff">Our Portfolio</div>
  <div class="shape" style="left:318px;top:90px;width:40px;height:40px;border-radius:50%;background:transparent;border:2px solid var(--ink)"></div>
  <div class="shape" style="left:18px;top:190px;width:66px;height:24px"></div>
  <div class="shape" style="left:128px;top:184px;width:64px;height:36px;background:var(--grey)"></div>
  <div class="shape" style="left:226px;top:190px;width:62px;height:24px;border-radius:12px;background:transparent;border:2px solid var(--ink)"></div>
  <div class="shape" style="left:318px;top:180px;width:40px;height:40px;border-radius:50%"></div>
  <div class="footer"><span class="mini"></span></div>
</section>

<!-- 16 three bullets -->
<section class="slide">
  <div class="title">Three Bullets Area</div>
  <div class="logo"><span class="logo-mark"></span>Varrenko</div>
  <div class="photo" style="left:0;top:44px;width:392px;height:100px" role="img" aria-label="Workshop interior with machinery"></div>
  <div class="dot ink" style="left:64px;top:128px;width:32px;height:32px;border:2px solid #fff">1</div>
  <div class="dot" style="left:180px;top:128px;width:32px;height:32px;border:2px solid #fff">2</div>
  <div class="dot ink" style="left:296px;top:128px;width:32px;height:32px;border:2px solid #fff">3</div>
  <div class="txt" style="left:30px;top:170px;width:100px;text-align:center"><span class="h">Reliable Service</span><br>Help when it is needed</div>
  <div class="txt" style="left:146px;top:170px;width:100px;text-align:center"><span class="h">Skilled People</span><br>Decades of know-how</div>
  <div class="txt" style="left:262px;top:170px;width:100px;text-align:center"><span class="h">Lasting Products</span><br>Built for long life</div>
  <div class="footer"><span class="mini"></span></div>
</section>

<!-- 17 four column -->
<section class="slide">
  <div class="title">Four Column Area</div>
  <div class="logo"><span class="logo-mark"></span>Varrenko</div>
  <div class="dot ink" style="left:40px;top:66px;width:34px;height:34px">01</div>
  <div class="dot" style="left:130px;top:66px;width:34px;height:34px">02</div>
  <div class="dot ink" style="left:220px;top:66px;width:34px;height:34px">03</div>
  <div class="dot grey" style="left:310px;top:66px;width:34px;height:34px">04</div>
  <div class="txt" style="left:17px;top:112px;width:80px;text-align:center"><span class="h">Maritime</span><br>Vessel systems and deck machines</div>
  <div class="txt" style="left:107px;top:112px;width:80px;text-align:center"><span class="h" style="color:var(--red)">Hydraulics</span><br>Cylinders and power units</div>
  <div class="txt" style="left:197px;top:112px;width:80px;text-align:center"><span class="h">Machinery</span><br>Heavy lifting equipment</div>
  <div class="txt" style="left:287px;top:112px;width:80px;text-align:center"><span class="h">Services</span><br>Repair and maintenance</div>
  <div class="footer"><span class="mini"></span></div>
</section>

<!-- 18 circle infographic -->
<section class="slide">
  <div class="title">Circle Infographic</div>
  <div class="logo"><span class="logo-mark"></span>Varrenko</div>
  <svg width="392" height="287" viewBox="0 0 392 287" style="left:0;top:0">
    <g fill="none" stroke-width="22" transform="rotate(-90 196 145)">
      <circle cx="196" cy="145" r="50" stroke="#e2474b" stroke-dasharray="74 240"/>
      <circle cx="196" cy="145" r="50" stroke="#3b3b3d" stroke-dasharray="74 240" stroke-dashoffset="-78.5"/>
      <circle cx="196" cy="145" r="50" stroke="#e2474b" stroke-dasharray="74 240" stroke-dashoffset="-157"/>
      <circle cx="196" cy="145" r="50" stroke="#3b3b3d" stroke-dasharray="74 240" stroke-dashoffset="-235.5"/>
    </g>
    <circle cx="196" cy="145" r="28" fill="#f4f4f5"/>
    <text x="196" y="148" text-anchor="middle" font-family="Raleway" font-weight="700" font-size="8" fill="#3b3b3d">Cycle</text>
    <g stroke="#b5b5b7"><line x1="110" y1="100" x2="150" y2="110"/><line x1="110" y1="190" x2="150" y2="180"/><line x1="282" y1="100" x2="242" y2="110"/><line x1="282" y1="190" x2="242" y2="180"/></g>
  </svg>
  <div class="txt" style="left:40px;top:92px;width:66px;text-align:right"><span class="h">Plan</span><br>Define the goal</div>
  <div class="txt" style="left:40px;top:182px;width:66px;text-align:right"><span class="h">Build</span><br>Make it real</div>
  <div class="txt" style="left:288px;top:92px;width:70px"><span class="h">Test</span><br>Check each part</div>
  <div class="txt" style="left:288px;top:182px;width:70px"><span class="h">Deliver</span><br>Hand over safely</div>
  <div class="footer"><span class="mini"></span></div>
</section>

<!-- 19-21 section breaks -->
<section class="slide dark">
  <div class="brand-block" style="left:18px;top:140px;width:80px;height:60px;font-size:9px"><span class="mark" style="width:18px;height:18px"></span>Varrenko</div>
  <div style="position:absolute;left:0;top:200px;width:392px;height:10px;background:var(--red)"></div>
  <div class="sec-title" style="left:20px;top:218px">Section Break</div>
  <div class="footer"><span class="mini"></span></div>
</section>
<section class="slide red">
  <div style="position:absolute;left:0;top:158px;width:392px;height:14px;background:var(--ink)"></div>
  <div class="brand-block" style="left:155px;top:110px;width:82px;height:62px;font-size:9px;background:var(--ink)"><span class="mark" style="width:18px;height:18px"></span>Varrenko</div>
  <div class="big" style="position:absolute;left:0;width:392px;top:184px;text-align:center;font-size:13px;color:#fff">Section Break</div>
  <div class="footer"><span class="mini"></span></div>
</section>
<section class="slide grey">
  <div style="position:absolute;left:150px;top:0;width:92px;height:287px;background:var(--red)"></div>
  <div class="brand-block" style="left:150px;top:110px;width:92px;height:62px;font-size:9px;background:var(--ink)"><span class="mark" style="width:18px;height:18px"></span>Varrenko</div>
  <div class="big" style="position:absolute;left:0;width:392px;top:184px;text-align:center;font-size:13px;color:#fff">Section Break</div>
  <div class="footer"><span class="mini"></span></div>
</section>

<!-- 22 global -->
<section class="slide">
  <div class="title">Global Experience</div>
  <div class="logo"><span class="logo-mark"></span>Varrenko</div>
  <div class="map" style="left:30px;top:54px;width:330px;height:150px" role="img" aria-label="Grey world map"></div>
  <svg width="392" height="287" style="left:0;top:0">
    <g fill="#3b3b3d">
      <path d="M112 92c-5 0-8 4-8 8 0 6 8 14 8 14s8-8 8-14c0-4-3-8-8-8z"/>
      <path d="M196 80c-5 0-8 4-8 8 0 6 8 14 8 14s8-8 8-14c0-4-3-8-8-8z"/>
      <path d="M272 120c-5 0-8 4-8 8 0 6 8 14 8 14s8-8 8-14c0-4-3-8-8-8z"/>
    </g>
    <path d="M222 100c-5 0-8 4-8 8 0 6 8 14 8 14s8-8 8-14c0-4-3-8-8-8z" fill="#e2474b"/>
    <g fill="#fff"><circle cx="112" cy="100" r="2.5"/><circle cx="196" cy="88" r="2.5"/><circle cx="272" cy="128" r="2.5"/><circle cx="222" cy="108" r="2.5"/></g>
  </svg>
  <div class="dot ink" style="left:30px;top:222px;width:12px;height:12px"></div><div class="txt" style="left:48px;top:219px"><span class="h">Heading Goes Here</span><br>Offices and service points worldwide</div>
  <div class="footer"><span class="mini"></span></div>
</section>

<!-- 23 portfolio area -->
<section class="slide">
  <div class="title">Portfolio Area</div>
  <div class="logo"><span class="logo-mark"></span>Varrenko</div>
  <div style="position:absolute;left:16px;top:48px;width:80px;height:3px;background:var(--red)"></div>
  <div class="photo" style="left:16px;top:60px;width:86px;height:60px" role="img" aria-label="Project photo"></div>
  <div class="photo warm" style="left:107px;top:60px;width:86px;height:60px" role="img" aria-label="Project photo"></div>
  <div class="photo" style="left:198px;top:60px;width:86px;height:60px" role="img" aria-label="Project photo"></div>
  <div class="photo warm" style="left:289px;top:60px;width:86px;height:60px" role="img" aria-label="Project photo"></div>
  <div style="position:absolute;left:16px;top:120px;width:359px;height:40px;background:var(--ink)"></div>
  <div class="txt" style="left:22px;top:128px;width:78px;color:#ddd"><b>Project One</b><br>Deck cranes</div>
  <div class="txt" style="left:113px;top:128px;width:78px;color:#ddd"><b>Project Two</b><br>Power units</div>
  <div class="txt" style="left:204px;top:128px;width:78px;color:#ddd"><b>Project Three</b><br>Lifting gear</div>
  <div class="txt" style="left:295px;top:128px;width:78px;color:#ddd"><b>Project Four</b><br>Yard service</div>
  <div class="footer"><span class="mini"></span></div>
</section>

<!-- 24 team -->
<section class="slide">
  <div class="title">Our Team</div>
  <div class="logo"><span class="logo-mark"></span>Varrenko</div>
  <div class="photo light round" style="left:60px;top:66px;width:84px;height:84px;border:3px solid var(--grey-light)" role="img" aria-label="Team member portrait"></div>
  <div class="big" style="position:absolute;left:164px;top:84px;font-size:10px;color:var(--ink)">Mikael Sorvo</div>
  <div class="txt" style="left:164px;top:99px">Head of Engineering</div>
  <div style="position:absolute;left:164px;top:114px;font-size:9px;color:var(--red);letter-spacing:2px">★★★★</div>
  <div class="footer"><span class="mini"></span></div>
</section>

<!-- 25 product mockup -->
<section class="slide">
  <div class="title">Product Mockup</div>
  <div class="logo"><span class="logo-mark"></span>Varrenko</div>
  <div style="position:absolute;left:16px;top:60px;width:190px;height:118px;background:var(--ink-deep);border-radius:4px;padding:6px"><div style="position:relative;width:100%;height:100%;background:#fff"><div class="brand-block" style="left:58px;top:30px;width:62px;height:46px;font-size:7px"><span class="mark" style="width:12px;height:12px"></span>Varrenko</div></div></div>
  <div style="position:absolute;left:98px;top:178px;width:26px;height:12px;background:var(--grey-mid)"></div>
  <div style="position:absolute;left:84px;top:190px;width:54px;height:3px;background:var(--grey-mid)"></div>
  <div class="dot" style="left:228px;top:68px;width:12px;height:12px"></div><div class="txt" style="left:246px;top:66px"><span class="h" style="color:var(--red)">Content Title</span><br>Clear slides for every talk</div>
  <div class="dot" style="left:228px;top:108px;width:12px;height:12px"></div><div class="txt" style="left:246px;top:106px"><span class="h" style="color:var(--red)">Content Title</span><br>Works on every screen</div>
  <div class="dot" style="left:228px;top:148px;width:12px;height:12px"></div><div class="txt" style="left:246px;top:146px"><span class="h" style="color:var(--red)">Content Title</span><br>Easy to edit and share</div>
  <div class="footer"><span class="mini"></span></div>
</section>

<!-- 26 chart title donuts -->
<section class="slide">
  <div class="title">Chart Title</div>
  <div class="logo"><span class="logo-mark"></span>Varrenko</div>
  <svg width="392" height="200" style="left:0;top:50px">
    <g fill="none" stroke-width="6" transform="rotate(-90 0 0)">
    </g>
    <g fill="none" stroke-width="6">
      <circle cx="56" cy="50" r="26" stroke="#e9e9ea"/><circle cx="56" cy="50" r="26" stroke="#3b3b3d" stroke-dasharray="120 200" transform="rotate(-90 56 50)"/>
      <circle cx="148" cy="50" r="26" stroke="#e9e9ea"/><circle cx="148" cy="50" r="26" stroke="#e2474b" stroke-dasharray="90 200" transform="rotate(-90 148 50)"/>
      <circle cx="240" cy="50" r="26" stroke="#e9e9ea"/><circle cx="240" cy="50" r="26" stroke="#3b3b3d" stroke-dasharray="60 200" transform="rotate(-90 240 50)"/>
      <circle cx="332" cy="50" r="26" stroke="#e9e9ea"/><circle cx="332" cy="50" r="26" stroke="#8c8c8e" stroke-dasharray="140 200" transform="rotate(-90 332 50)"/>
    </g>
    <g font-family="Raleway" font-weight="700" font-size="8" text-anchor="middle">
      <text x="56" y="53" fill="#3b3b3d">73%</text><text x="148" y="53" fill="#e2474b">55%</text><text x="240" y="53" fill="#3b3b3d">37%</text><text x="332" y="53" fill="#8c8c8e">86%</text>
    </g>
  </svg>
  <div class="big" style="position:absolute;left:16px;width:80px;text-align:center;top:142px;font-size:10px">$9,752</div>
  <div class="big" style="position:absolute;left:108px;width:80px;text-align:center;top:142px;font-size:10px;color:var(--red)">100,895</div>
  <div class="big" style="position:absolute;left:200px;width:80px;text-align:center;top:142px;font-size:10px">5,508</div>
  <div class="big" style="position:absolute;left:292px;width:80px;text-align:center;top:142px;font-size:10px;color:var(--grey)">25,902</div>
  <div class="txt" style="left:16px;width:80px;text-align:center;top:158px">Revenue</div>
  <div class="txt" style="left:108px;width:80px;text-align:center;top:158px">Units sold</div>
  <div class="txt" style="left:200px;width:80px;text-align:center;top:158px">Customers</div>
  <div class="txt" style="left:292px;width:80px;text-align:center;top:158px">Hours</div>
  <div class="footer"><span class="mini"></span></div>
</section>

<!-- 27 price slide -->
<section class="slide">
  <div class="title">Price Slide</div>
  <div class="logo"><span class="logo-mark"></span>Varrenko</div>
  <div style="position:absolute;left:16px;top:44px;width:360px;height:186px;display:grid;grid-template-columns:repeat(4,1fr);gap:4px">
    <div style="background:var(--grey-pale)"><div class="big" style="height:38px;background:var(--ink);color:#fff;font-size:11px;display:flex;align-items:center;justify-content:center">$100</div><div class="txt" style="position:static;padding:10px 8px;text-align:center">Basic parts<br>Email help<br>1 site<br>Yearly check</div></div>
    <div style="background:var(--grey-pale)"><div class="big" style="height:38px;background:var(--red);color:#fff;font-size:11px;display:flex;align-items:center;justify-content:center">$200</div><div class="txt" style="position:static;padding:10px 8px;text-align:center">All parts<br>Phone help<br>2 sites<br>Half year check</div></div>
    <div style="background:var(--grey-pale)"><div class="big" style="height:38px;background:var(--ink);color:#fff;font-size:11px;display:flex;align-items:center;justify-content:center">$300</div><div class="txt" style="position:static;padding:10px 8px;text-align:center">All parts<br>On site help<br>5 sites<br>Quarter check</div></div>
    <div style="background:var(--grey-pale)"><div class="big" style="height:38px;background:var(--red);color:#fff;font-size:11px;display:flex;align-items:center;justify-content:center">$400</div><div class="txt" style="position:static;padding:10px 8px;text-align:center">Full care<br>24h help<br>All sites<br>Monthly check</div></div>
  </div>
  <div class="footer"><span class="mini"></span></div>
</section>

<!-- 28 pricing plan -->
<section class="slide">
  <div class="title">Pricing Table Plan</div>
  <div class="logo"><span class="logo-mark"></span>Varrenko</div>
  <div class="dot ink" style="left:38px;top:62px;width:22px;height:22px"></div>
  <div class="dot grey" style="left:128px;top:62px;width:22px;height:22px"></div>
  <div class="dot" style="left:218px;top:62px;width:22px;height:22px"></div>
  <div class="dot ink" style="left:308px;top:62px;width:22px;height:22px"></div>
  <div class="big" style="position:absolute;left:9px;width:80px;text-align:center;top:94px;font-size:18px">$10</div>
  <div class="big" style="position:absolute;left:99px;width:80px;text-align:center;top:94px;font-size:18px;color:var(--grey)">$20</div>
  <div class="big" style="position:absolute;left:189px;width:80px;text-align:center;top:94px;font-size:18px;color:var(--red)">$40</div>
  <div class="big" style="position:absolute;left:279px;width:80px;text-align:center;top:94px;font-size:18px">$50</div>
  <div class="txt" style="left:9px;width:80px;text-align:center;top:124px"><span class="h">Basic</span><br>One user<br>Email help</div>
  <div class="txt" style="left:99px;width:80px;text-align:center;top:124px"><span class="h">Starter</span><br>Three users<br>Email help</div>
  <div class="txt" style="left:189px;width:80px;text-align:center;top:124px"><span class="h">Business</span><br>Ten users<br>Phone help</div>
  <div class="txt" style="left:279px;width:80px;text-align:center;top:124px"><span class="h">Premium</span><br>All users<br>24h help</div>
  <div class="footer"><span class="mini"></span></div>
</section>

<!-- 29 social media -->
<section class="slide">
  <div class="title">Social Media Marketing</div>
  <div class="logo"><span class="logo-mark"></span>Varrenko</div>
  <div style="position:absolute;left:110px;top:82px;width:26px;height:150px;background:var(--ink)"></div>
  <div style="position:absolute;left:160px;top:116px;width:26px;height:116px;background:var(--red)"></div>
  <div style="position:absolute;left:210px;top:94px;width:26px;height:138px;background:var(--grey-mid)"></div>
  <div style="position:absolute;left:260px;top:166px;width:26px;height:66px;background:var(--grey-mid)"></div>
  <div class="dot ink" style="left:110px;top:50px;width:26px;height:26px">A</div>
  <div class="dot" style="left:160px;top:50px;width:26px;height:26px">B</div>
  <div class="dot grey" style="left:210px;top:50px;width:26px;height:26px">C</div>
  <div class="dot grey" style="left:260px;top:50px;width:26px;height:26px">D</div>
  <div class="footer"><span class="mini"></span></div>
</section>

<!-- 30 pie chart -->
<section class="slide">
  <div class="title">3d Pie Chart</div>
  <div class="logo"><span class="logo-mark"></span>Varrenko</div>
  <div class="txt" style="left:70px;top:66px"><span class="h">Sales Report</span></div>
  <svg width="160" height="120" style="left:40px;top:82px">
    <ellipse cx="80" cy="66" rx="70" ry="36" fill="#2a2a2c"/>
    <ellipse cx="80" cy="56" rx="70" ry="36" fill="#8c8c8e"/>
    <path d="M80 56 L150 56 A70 36 0 0 1 60 91 Z" fill="#e2474b"/>
    <path d="M80 56 L60 91 A70 36 0 0 1 10 56 Z" fill="#3b3b3d"/>
  </svg>
  <div class="dot ink" style="left:250px;top:96px;width:9px;height:9px"></div><div class="lbl" style="left:264px;top:95px">Series one — 24%</div>
  <div class="dot" style="left:250px;top:116px;width:9px;height:9px"></div><div class="lbl" style="left:264px;top:115px">Series two — 31%</div>
  <div class="dot grey" style="left:250px;top:136px;width:9px;height:9px"></div><div class="lbl" style="left:264px;top:135px">Series three — 45%</div>
  <div class="footer"><span class="mini"></span></div>
</section>

<!-- 31 bar chart -->
<section class="slide">
  <div class="title">Bar Chart</div>
  <div class="logo"><span class="logo-mark"></span>Varrenko</div>
  <svg width="392" height="200" style="left:0;top:50px">
    <g stroke="#eee"><line x1="30" y1="40" x2="370" y2="40"/><line x1="30" y1="80" x2="370" y2="80"/><line x1="30" y1="120" x2="370" y2="120"/></g>
    <line x1="30" y1="160" x2="370" y2="160" stroke="#ccc"/>
    <g fill="#3b3b3d"><rect x="46" y="70" width="14" height="90"/><rect x="130" y="90" width="14" height="70"/><rect x="214" y="60" width="14" height="100"/><rect x="298" y="80" width="14" height="80"/></g>
    <g fill="#e2474b"><rect x="62" y="100" width="14" height="60"/><rect x="146" y="60" width="14" height="100"/><rect x="230" y="110" width="14" height="50"/><rect x="314" y="70" width="14" height="90"/></g>
    <g fill="#b5b5b7"><rect x="78" y="80" width="14" height="80"/><rect x="162" y="110" width="14" height="50"/><rect x="246" y="80" width="14" height="80"/><rect x="330" y="100" width="14" height="60"/></g>
    <g font-family="Open Sans" font-size="6" fill="#8c8c8e" text-anchor="middle"><text x="69" y="172">Q1</text><text x="153" y="172">Q2</text><text x="237" y="172">Q3</text><text x="321" y="172">Q4</text></g>
  </svg>
  <div class="footer"><span class="mini"></span></div>
</section>

<!-- 32 column charts -->
<section class="slide">
  <div class="title">Column Charts</div>
  <div class="logo"><span class="logo-mark"></span>Varrenko</div>
  <svg width="250" height="180" style="left:16px;top:56px">
    <line x1="0" y1="140" x2="240" y2="140" stroke="#ccc"/>
    <g fill="#3b3b3d"><rect x="12" y="60" width="16" height="80"/><rect x="72" y="80" width="16" height="60"/><rect x="132" y="50" width="16" height="90"/><rect x="192" y="70" width="16" height="70"/></g>
    <g fill="#e2474b"><rect x="30" y="90" width="16" height="50"/><rect x="90" y="50" width="16" height="90"/><rect x="150" y="100" width="16" height="40"/><rect x="210" y="80" width="16" height="60"/></g>
  </svg>
  <div class="txt" style="left:284px;top:76px;width:90px"><span class="h" style="color:var(--red)">Content Title</span><br>Orders grew in spring</div>
  <div class="txt" style="left:284px;top:126px;width:90px"><span class="h" style="color:var(--red)">Content Title</span><br>Service stayed steady</div>
  <div class="footer"><span class="mini"></span></div>
</section>

<!-- 33 financial -->
<section class="slide">
  <div class="title">Financial Slides</div>
  <div class="logo"><span class="logo-mark"></span>Varrenko</div>
  <div class="txt" style="left:110px;top:52px"><span class="h">Chart Title</span></div>
  <svg width="392" height="200" style="left:0;top:50px">
    <line x1="30" y1="150" x2="250" y2="150" stroke="#ccc"/>
    <polyline points="40,120 90,60 140,100 190,40 240,90" fill="none" stroke="#e2474b" stroke-width="2"/>
    <polyline points="40,90 90,110 140,70 190,90 240,60" fill="none" stroke="#3b3b3d" stroke-width="2"/>
    <line x1="262" y1="150" x2="370" y2="150" stroke="#ccc"/>
    <g fill="#e2474b"><rect x="270" y="80" width="10" height="70"/><rect x="300" y="60" width="10" height="90"/><rect x="330" y="90" width="10" height="60"/></g>
    <g fill="#3b3b3d"><rect x="282" y="100" width="10" height="50"/><rect x="312" y="110" width="10" height="40"/><rect x="342" y="70" width="10" height="80"/></g>
  </svg>
  <div class="footer"><span class="mini"></span></div>
</section>

<!-- 34 area chart -->
<section class="slide">
  <div class="title">Area Chart</div>
  <div class="logo"><span class="logo-mark"></span>Varrenko</div>
  <svg width="200" height="110" style="left:16px;top:50px">
    <path d="M0 100 L0 70 C40 20 80 60 120 30 S180 40 200 50 L200 100 Z" fill="#3b3b3d"/>
    <path d="M0 100 L0 85 C50 60 90 90 140 60 S190 70 200 75 L200 100 Z" fill="#e2474b"/>
  </svg>
  <div class="txt" style="left:16px;top:170px">Chart Analysis</div>
  <div class="big" style="position:absolute;left:16px;top:182px;font-size:20px;color:var(--red)">$27M</div>
  <div class="dot ink" style="left:246px;top:66px;width:18px;height:18px"></div><div class="txt" style="left:272px;top:66px"><span class="h">Revenue</span><br>Up 12% this year</div>
  <div class="dot" style="left:246px;top:106px;width:18px;height:18px"></div><div class="txt" style="left:272px;top:106px"><span class="h">Growth</span><br>New markets open</div>
  <div class="dot ink" style="left:246px;top:146px;width:18px;height:18px"></div><div class="txt" style="left:272px;top:146px"><span class="h">Margin</span><br>Stable and healthy</div>
  <div class="footer"><span class="mini"></span></div>
</section>

<!-- 35 table -->
<section class="slide">
  <div class="title">Table Slide</div>
  <div class="logo"><span class="logo-mark"></span>Varrenko</div>
  <table style="position:absolute;left:30px;top:50px;width:332px;font-size:6px;color:var(--grey)">
    <tr style="background:var(--ink);color:#fff;height:17px"><th>Item</th><th>Q1</th><th>Q2</th><th>Q3</th><th>Q4</th></tr>
    <tr style="height:17px;background:var(--grey-pale)"><td>Maritime</td><td>12</td><td>14</td><td>16</td><td>18</td></tr>
    <tr style="height:17px"><td>Hydraulics</td><td>10</td><td>11</td><td>13</td><td>15</td></tr>
    <tr style="height:17px;background:var(--grey-pale)"><td>Machinery</td><td>9</td><td>12</td><td>12</td><td>14</td></tr>
    <tr style="height:17px"><td>Services</td><td>7</td><td>8</td><td>9</td><td>11</td></tr>
    <tr style="height:17px;background:var(--grey-pale)"><td>Parts</td><td>5</td><td>6</td><td>6</td><td>8</td></tr>
    <tr style="height:17px"><td>Other</td><td>3</td><td>4</td><td>4</td><td>5</td></tr>
  </table>
  <div class="footer"><span class="mini"></span></div>
</section>

<!-- 36 team four -->
<section class="slide">
  <div class="title">Our Team</div>
  <div class="logo"><span class="logo-mark"></span>Varrenko</div>
  <div class="photo light round" style="left:50px;top:55px;width:40px;height:40px" role="img" aria-label="Team member portrait"></div><div class="txt" style="left:98px;top:62px"><span class="h">Anna Lepp</span><br>Sales Director</div>
  <div class="photo light round" style="left:220px;top:55px;width:40px;height:40px" role="img" aria-label="Team member portrait"></div><div class="txt" style="left:268px;top:62px"><span class="h">Jari Koski</span><br>Plant Manager</div>
  <div class="photo light round" style="left:50px;top:140px;width:40px;height:40px" role="img" aria-label="Team member portrait"></div><div class="txt" style="left:98px;top:147px"><span class="h">Ville Aho</span><br>Lead Engineer</div>
  <div class="photo light round" style="left:220px;top:140px;width:40px;height:40px" role="img" aria-label="Team member portrait"></div><div class="txt" style="left:268px;top:147px"><span class="h">Sari Niemi</span><br>Service Head</div>
  <div class="footer"><span class="mini"></span></div>
</section>

<!-- 37 project recondition -->
<section class="slide">
  <div class="title">Project Recondition</div>
  <div class="logo"><span class="logo-mark"></span>Varrenko</div>
  <div style="position:absolute;left:16px;top:36px;width:90px;height:3px;background:var(--red)"></div>
  <div class="photo" style="left:16px;top:56px;width:110px;height:34px" role="img" aria-label="Truck illustration"></div><div class="big" style="position:absolute;left:136px;top:58px;font-size:12px;color:var(--red)">80%</div><div class="txt" style="left:136px;top:75px">Fleet ready</div>
  <div class="photo" style="left:16px;top:110px;width:110px;height:34px" role="img" aria-label="Truck illustration"></div><div class="big" style="position:absolute;left:136px;top:112px;font-size:12px">65%</div><div class="txt" style="left:136px;top:129px">In repair</div>
  <div class="photo" style="left:16px;top:164px;width:110px;height:34px" role="img" aria-label="Truck illustration"></div><div class="big" style="position:absolute;left:136px;top:166px;font-size:12px;color:var(--red)">28%</div><div class="txt" style="left:136px;top:183px">Waiting</div>
  <div style="position:absolute;left:232px;top:56px;width:144px;height:62px;background:var(--ink)"></div>
  <div style="position:absolute;left:232px;top:126px;width:144px;height:62px;background:var(--ink)"></div>
  <div class="txt" style="left:242px;top:64px;width:124px;color:#ddd"><b style="color:#fff">Delivery Plan</b><br>Units leave the yard in order of need.</div>
  <div class="txt" style="left:242px;top:134px;width:124px;color:#ddd"><b style="color:#fff">Service Plan</b><br>Each unit gets a full check.</div>
  <div class="footer"><span class="mini"></span></div>
</section>

<!-- 38 system structure -->
<section class="slide">
  <div class="title">System Structure</div>
  <div class="logo"><span class="logo-mark"></span>Varrenko</div>
  <svg width="200" height="170" style="left:20px;top:54px">
    <polygon points="100,0 140,60 60,60" fill="#e2474b"/>
    <polygon points="56,66 144,66 180,120 20,120" fill="#3b3b3d"/>
    <polygon points="16,126 184,126 200,150 0,150" fill="#8c8c8e"/>
  </svg>
  <div class="txt" style="left:236px;top:80px;width:136px"><span class="h">Strategy</span><br>Leadership and long term goals</div>
  <div class="txt" style="left:236px;top:130px;width:136px"><span class="h">Operations</span><br>Plants, services and people</div>
  <div class="txt" style="left:236px;top:180px;width:136px"><span class="h">Foundation</span><br>Values, safety and trust</div>
  <div class="footer"><span class="mini"></span></div>
</section>

<!-- 39 idea in detail -->
<section class="slide">
  <div class="title">Idea in Detail</div>
  <div class="logo"><span class="logo-mark"></span>Varrenko</div>
  <svg width="392" height="200" style="left:0;top:40px">
    <polygon points="150,100 392,10 392,190" fill="#e2474b"/>
    <polygon points="190,110 392,50 392,170" fill="#3b3b3d"/>
    <polygon points="230,115 392,85 392,145" fill="#b5b5b7"/>
  </svg>
  <div class="dot" style="left:20px;top:68px;width:14px;height:14px"></div><div class="txt" style="left:42px;top:66px"><span class="h">First Idea</span><br>Start small</div>
  <div class="dot ink" style="left:20px;top:118px;width:14px;height:14px"></div><div class="txt" style="left:42px;top:116px"><span class="h">Second Idea</span><br>Test it well</div>
  <div class="dot grey" style="left:20px;top:168px;width:14px;height:14px"></div><div class="txt" style="left:42px;top:166px"><span class="h">Third Idea</span><br>Grow it wide</div>
  <div class="footer"><span class="mini"></span></div>
</section>

<!-- 40 achievement -->
<section class="slide">
  <div class="title">Achivement Disclosure</div>
  <div class="logo"><span class="logo-mark"></span>Varrenko</div>
  <div style="position:absolute;left:30px;top:140px;width:30px;height:80px;background:var(--ink)"></div>
  <div style="position:absolute;left:62px;top:110px;width:30px;height:110px;background:var(--red)"></div>
  <div style="position:absolute;left:94px;top:80px;width:30px;height:140px;background:var(--ink)"></div>
  <div style="position:absolute;left:126px;top:100px;width:30px;height:120px;background:var(--red)"></div>
  <div style="position:absolute;left:158px;top:130px;width:30px;height:90px;background:var(--grey)"></div>
  <div class="dot" style="left:212px;top:80px;width:10px;height:10px"></div><div class="txt" style="left:230px;top:77px"><span class="h">2015</span> First milestone</div>
  <div class="dot ink" style="left:212px;top:120px;width:10px;height:10px"></div><div class="txt" style="left:230px;top:117px"><span class="h">2016</span> New markets</div>
  <div class="dot" style="left:212px;top:160px;width:10px;height:10px"></div><div class="txt" style="left:230px;top:157px"><span class="h">2017</span> Record year</div>
  <div class="footer"><span class="mini"></span></div>
</section>

<!-- 41 gear component -->
<section class="slide">
  <div class="title">Gear Component</div>
  <div class="logo"><span class="logo-mark"></span>Varrenko</div>
  <svg width="392" height="287" style="left:0;top:0">
    <g fill="none" stroke-width="26" transform="rotate(-90 196 140)">
      <circle cx="196" cy="140" r="46" stroke="#e2474b" stroke-dasharray="68 221"/>
      <circle cx="196" cy="140" r="46" stroke="#3b3b3d" stroke-dasharray="68 221" stroke-dashoffset="-72.3"/>
      <circle cx="196" cy="140" r="46" stroke="#8c8c8e" stroke-dasharray="68 221" stroke-dashoffset="-144.6"/>
      <circle cx="196" cy="140" r="46" stroke="#3b3b3d" stroke-dasharray="68 221" stroke-dashoffset="-216.9"/>
    </g>
    <circle cx="196" cy="140" r="22" fill="#e2474b"/>
    <circle cx="196" cy="140" r="9" fill="#fff"/>
    <g stroke="#b5b5b7"><line x1="96" y1="98" x2="140" y2="110"/><line x1="96" y1="182" x2="140" y2="170"/><line x1="296" y1="98" x2="252" y2="110"/><line x1="296" y1="182" x2="252" y2="170"/></g>
  </svg>
  <div class="txt" style="left:24px;top:90px;width:70px;text-align:right"><span class="h">Process</span><br>Smooth flow</div>
  <div class="txt" style="left:24px;top:174px;width:70px;text-align:right"><span class="h">Quality</span><br>No defects</div>
  <div class="txt" style="left:300px;top:90px;width:70px"><span class="h" style="color:var(--red)">Design</span><br>Smart parts</div>
  <div class="txt" style="left:300px;top:174px;width:70px"><span class="h">Build</span><br>Solid work</div>
  <div class="footer"><span class="mini"></span></div>
</section>

<!-- 42 time exposure -->
<section class="slide">
  <div class="title">Time Exposure</div>
  <div class="logo"><span class="logo-mark"></span>Varrenko</div>
  <svg width="392" height="287" style="left:0;top:0">
    <circle cx="196" cy="140" r="48" fill="#f4f4f5" stroke="#3b3b3d" stroke-width="6"/>
    <line x1="196" y1="140" x2="196" y2="108" stroke="#3b3b3d" stroke-width="4" stroke-linecap="round"/>
    <line x1="196" y1="140" x2="220" y2="152" stroke="#e2474b" stroke-width="4" stroke-linecap="round"/>
    <circle cx="196" cy="140" r="5" fill="#e2474b"/>
    <g fill="#e2474b"><circle cx="128" cy="96" r="12"/><circle cx="264" cy="184" r="12"/></g>
    <g fill="#3b3b3d"><circle cx="264" cy="96" r="12"/><circle cx="128" cy="184" r="12"/></g>
  </svg>
  <div class="txt" style="left:30px;top:88px;width:80px;text-align:right"><span class="h">Planning</span><br>Set the schedule</div>
  <div class="txt" style="left:30px;top:176px;width:80px;text-align:right"><span class="h">Tracking</span><br>Follow each task</div>
  <div class="txt" style="left:284px;top:88px;width:90px"><span class="h">Results</span><br>Measure the gain</div>
  <div class="txt" style="left:284px;top:176px;width:90px"><span class="h">Review</span><br>Learn and adjust</div>
  <div class="footer"><span class="mini"></span></div>
</section>

<!-- 43 increasing amount -->
<section class="slide">
  <div class="title">Increasing Amount</div>
  <div class="logo"><span class="logo-mark"></span>Varrenko</div>
  <svg width="392" height="200" style="left:0;top:40px">
    <g fill="none" stroke-width="22" transform="rotate(-90 196 100)">
      <circle cx="196" cy="100" r="46" stroke="#3b3b3d" stroke-dasharray="68 221"/>
      <circle cx="196" cy="100" r="46" stroke="#e2474b" stroke-dasharray="68 221" stroke-dashoffset="-72.3"/>
      <circle cx="196" cy="100" r="46" stroke="#8c8c8e" stroke-dasharray="68 221" stroke-dashoffset="-144.6"/>
      <circle cx="196" cy="100" r="46" stroke="#3b3b3d" stroke-dasharray="68 221" stroke-dashoffset="-216.9"/>
    </g>
    <text x="196" y="104" text-anchor="middle" font-family="Raleway" font-weight="700" font-size="10" fill="#e2474b">+24%</text>
  </svg>
  <div class="txt" style="left:40px;top:86px;width:90px"><span class="h" style="color:var(--red)">Progress</span><br>Steady steps</div>
  <div class="txt" style="left:40px;top:168px;width:90px"><span class="h">Dedication</span><br>Strong teams</div>
  <div class="txt" style="left:280px;top:86px;width:90px"><span class="h" style="color:var(--red)">Innovation</span><br>New solutions</div>
  <div class="txt" style="left:280px;top:168px;width:90px"><span class="h">Technology</span><br>Modern tools</div>
  <div class="footer"><span class="mini"></span></div>
</section>

<!-- 44 gear diagram -->
<section class="slide">
  <div class="title">Gear Diagram</div>
  <div class="logo"><span class="logo-mark"></span>Varrenko</div>
  <svg width="392" height="287" style="left:0;top:0">
    <g fill="none" stroke-width="12">
      <circle cx="96" cy="110" r="32" stroke="#3b3b3d" stroke-dasharray="14 6"/>
      <circle cx="160" cy="170" r="28" stroke="#e2474b" stroke-dasharray="14 6"/>
      <circle cx="206" cy="96" r="24" stroke="#8c8c8e" stroke-dasharray="12 6"/>
    </g>
    <g font-family="Raleway" font-weight="700" font-size="8" text-anchor="middle"><text x="96" y="113" fill="#3b3b3d">01</text><text x="160" y="173" fill="#e2474b">02</text><text x="206" y="99" fill="#8c8c8e">03</text></g>
    <g stroke="#b5b5b7"><line x1="232" y1="96" x2="262" y2="76"/><line x1="188" y1="170" x2="262" y2="176"/><line x1="128" y1="110" x2="262" y2="126"/></g>
  </svg>
  <div class="txt" style="left:268px;top:68px;width:110px"><span class="h">Heading One</span><br>Design and planning</div>
  <div class="txt" style="left:268px;top:118px;width:110px"><span class="h">Heading Two</span><br>Production steps</div>
  <div class="txt" style="left:268px;top:168px;width:110px"><span class="h" style="color:var(--red)">Heading Three</span><br>Delivery and care</div>
  <div class="footer"><span class="mini"></span></div>
</section>

<!-- 45 europe map -->
<section class="slide">
  <div class="title">Europe Map</div>
  <div class="map" style="left:150px;top:40px;width:226px;height:200px" role="img" aria-label="Grey map of Europe"></div>
  <div class="txt" style="left:16px;top:44px"><span class="big" style="font-size:12px;color:var(--red)">$12M</span><br>Nordic sales</div>
  <div class="txt" style="left:16px;top:80px"><span class="big" style="font-size:12px;color:var(--red)">$26M</span><br>Central Europe</div>
  <div class="dot" style="left:236px;top:66px;width:36px;height:36px">42%</div>
  <div class="dot ink" style="left:190px;top:130px;width:36px;height:36px">27%</div>
  <div class="dot ink" style="left:290px;top:150px;width:36px;height:36px">18%</div>
  <div class="dot grey" style="left:300px;top:90px;width:30px;height:30px">13%</div>
  <div class="footer"><span class="mini"></span></div>
</section>

<!-- 46 gantt month -->
<section class="slide">
  <div class="title">Gantt Chart (One Month)</div>
  <div class="logo"><span class="logo-mark"></span>Varrenko</div>
  <div style="position:absolute;left:16px;top:50px;width:360px;height:14px;background:var(--ink)"></div>
  <div class="txt" style="left:22px;top:53px;color:#fff">Task &nbsp;&nbsp;&nbsp;&nbsp;&nbsp;&nbsp;&nbsp;&nbsp;&nbsp;&nbsp; Week 1 &nbsp;&nbsp;&nbsp;&nbsp;&nbsp;&nbsp;&nbsp;&nbsp;&nbsp;&nbsp;&nbsp;&nbsp;&nbsp; Week 2 &nbsp;&nbsp;&nbsp;&nbsp;&nbsp;&nbsp;&nbsp;&nbsp;&nbsp;&nbsp;&nbsp;&nbsp;&nbsp; Week 3 &nbsp;&nbsp;&nbsp;&nbsp;&nbsp;&nbsp;&nbsp;&nbsp;&nbsp;&nbsp;&nbsp;&nbsp;&nbsp; Week 4</div>
  <div style="position:absolute;left:16px;top:64px;width:360px;height:120px;background:repeating-linear-gradient(var(--grey-pale) 0 15px,#fff 15px 30px)"></div>
  <div class="txt" style="left:22px;top:68px;line-height:30px">Design<br>Parts<br>Assembly<br>Testing</div>
  <div style="position:absolute;left:90px;top:72px;width:80px;height:7px;background:var(--red)"></div>
  <div style="position:absolute;left:140px;top:102px;width:120px;height:7px;background:var(--ink)"></div>
  <div style="position:absolute;left:200px;top:132px;width:90px;height:7px;background:var(--red)"></div>
  <div style="position:absolute;left:260px;top:162px;width:100px;height:7px;background:var(--ink)"></div>
  <div class="footer"><span class="mini"></span></div>
</section>

<!-- 47 gantt year -->
<section class="slide">
  <div class="title">Gantt Chart (One Year)</div>
  <div class="logo"><span class="logo-mark"></span>Varrenko</div>
  <div style="position:absolute;left:16px;top:50px;width:360px;height:14px;background:var(--ink)"></div>
  <div class="txt" style="left:22px;top:53px;color:#fff">Task &nbsp;&nbsp;&nbsp;&nbsp;&nbsp;&nbsp;&nbsp;&nbsp;&nbsp;&nbsp; Q1 &nbsp;&nbsp;&nbsp;&nbsp;&nbsp;&nbsp;&nbsp;&nbsp;&nbsp;&nbsp;&nbsp;&nbsp;&nbsp;&nbsp;&nbsp;&nbsp;&nbsp;&nbsp;&nbsp; Q2 &nbsp;&nbsp;&nbsp;&nbsp;&nbsp;&nbsp;&nbsp;&nbsp;&nbsp;&nbsp;&nbsp;&nbsp;&nbsp;&nbsp;&nbsp;&nbsp;&nbsp;&nbsp;&nbsp; Q3 &nbsp;&nbsp;&nbsp;&nbsp;&nbsp;&nbsp;&nbsp;&nbsp;&nbsp;&nbsp;&nbsp;&nbsp;&nbsp;&nbsp;&nbsp;&nbsp;&nbsp;&nbsp;&nbsp; Q4</div>
  <div style="position:absolute;left:16px;top:64px;width:360px;height:150px;background:repeating-linear-gradient(var(--grey-pale) 0 15px,#fff 15px 30px)"></div>
  <div class="txt" style="left:22px;top:68px;line-height:15px">Study<br>Design<br>Sourcing<br>Parts<br>Build<br>Test<br>Ship<br>Review<br>Service<br>Close</div>
  <div style="position:absolute;left:80px;top:68px;width:60px;height:7px;background:var(--red)"></div>
  <div style="position:absolute;left:110px;top:83px;width:90px;height:7px;background:var(--ink)"></div>
  <div style="position:absolute;left:150px;top:113px;width:70px;height:7px;background:var(--red)"></div>
  <div style="position:absolute;left:190px;top:143px;width:100px;height:7px;background:var(--ink)"></div>
  <div style="position:absolute;left:250px;top:173px;width:90px;height:7px;background:var(--red)"></div>
  <div style="position:absolute;left:300px;top:203px;width:60px;height:7px;background:var(--ink)"></div>
  <div class="footer"><span class="mini"></span></div>
</section>

<!-- 48 thank you -->
<section class="slide dark">
  <div class="photo" style="inset:0;background:linear-gradient(135deg,#3a2220,#1f1f22 60%,#5a2a26)" role="img" aria-label="Dark photo of sparks in a workshop"></div>
  <div class="brand-block" style="left:20px;top:110px;width:110px;height:80px;font-size:11px"><span class="mark" style="width:24px;height:24px"></span>Varrenko</div>
  <div class="big" style="position:absolute;left:230px;top:128px;font-size:22px;color:#fff">Thank You</div>
  <div class="txt" style="left:262px;top:158px;color:#ddd">Varrenko Ltd.</div>
</section>

</main>
</body>
</html>
```